Website for Kitchen Showroom

We need a website for our Kitchen Showroom. Will be 10 pages in total. Example of a website we like can be found at http://www.brivantaform.co.uk/ with the image on the front page being a java script slideshow picking up images from a directory that I can update. Looking for simple SEO
I have the wording/ sitemap/ images all ready to go and I am looking for a quick turn around.
Thank you for your time. Tom

```html
<!DOCTYPE html>
<html lang="en">
<head>
<meta charset="utf-8">
<title>Kitchen Atelier – Designer Kitchens</title>
<link href="https://fonts.googleapis.com/css2?family=Ubuntu:wght@300;400;500&family=Noto+Sans:wght@400&display=swap" rel="stylesheet">
<style>
:root{
  --bg:#050605;
  --nav-top:#2e2f2e;
  --nav-bottom:#0b0b0b;
  --nav-line:#3a3a3a;
  --nav-text:#a9a9a9;
  --nav-active:#ffffff;
  --green:#6fbf2a;
  --green-deep:#1d3a0a;
  --logo-grey:#b9b9b9;
  --text:#6c6c6c;
  --text-bright:#f2f2f2;
  --link:#8cd13c;
  --frame:#0d0d0d;
  --dots:#4a4a4a;
}
*{box-sizing:border-box;margin:0;padding:0}
html,body{width:1200px;height:992px;overflow:hidden}
body{
  position:relative;
  background:
    radial-gradient(ellipse 520px 130px at 600px 120px, rgba(46,92,14,.55), transparent 70%),
    radial-gradient(ellipse 620px 180px at 600px 640px, rgba(40,86,10,.55), transparent 70%),
    radial-gradient(ellipse 520px 260px at 600px 410px, rgba(24,52,6,.6), transparent 75%),
    var(--bg);
  font-family:"Noto Sans",Tahoma,sans-serif;
  color:var(--text);
}
.site-nav{
  position:absolute;left:0;top:0;width:1200px;height:40px;
  background:linear-gradient(var(--nav-top),var(--nav-bottom));
  border-bottom:2px solid #1a1a1a;
}
.site-nav ul{list-style:none;position:absolute;left:122px;top:0;display:flex;height:38px}
.site-nav li{border-right:1px solid var(--nav-line);height:38px}
.site-nav a{
  display:block;padding:0 19px;line-height:36px;
  font-family:"Ubuntu",sans-serif;font-weight:500;font-size:12.5px;
  color:var(--nav-text);text-decoration:none;
}
.site-nav .is-active a{color:var(--nav-active)}
.brand{position:absolute;left:142px;top:66px;display:flex;align-items:center;gap:10px}
.brand-mark{width:18px;height:18px;background:var(--green)}
.brand-name{
  font-family:"Ubuntu",sans-serif;font-weight:300;font-size:34px;line-height:30px;
  color:var(--logo-grey);
}
.search{
  position:absolute;left:900px;top:107px;width:156px;height:21px;
  background:#141414;border:1px solid #2e2e2e;display:flex;align-items:center;
}
.search span{flex:1;padding-left:8px;font-size:10px;color:#9a9a9a}
.search .search-btn{width:19px;height:19px;background:#cfcfcf;display:flex;align-items:center;justify-content:center}
.glow-line{
  position:absolute;left:205px;width:790px;height:2px;
  background:linear-gradient(90deg,transparent,var(--green) 30%,var(--green) 70%,transparent);
  opacity:.55;
}
.thumb{
  position:absolute;left:142px;width:230px;height:97px;
  border:2px solid var(--frame);box-shadow:0 0 0 1px #222;
}
.hero{
  position:absolute;left:386px;top:175px;width:673px;height:433px;
  border:3px solid var(--frame);box-shadow:0 0 0 1px #222;
  background:linear-gradient(100deg,#d9ccaa 0%,#cdbb94 30%,#a0492e 62%,#c9a98a 80%,#e6dcc0 100%);
}
.social-label{position:absolute;left:142px;top:687px;font-size:9.5px;color:#8a8a8a}
.social{
  position:absolute;left:142px;width:160px;height:21px;
  background:linear-gradient(90deg,#2a2a2a,#1a1a1a 70%,transparent);
  font-size:9.5px;color:#a0a0a0;line-height:21px;padding-left:6px;letter-spacing:.3px;
}
.content-title{
  position:absolute;left:383px;top:686px;
  font-family:"Ubuntu",sans-serif;font-weight:500;font-size:13px;color:var(--text-bright);
  display:flex;align-items:center;gap:8px;
}
.content-title i{width:7px;height:7px;background:#8a8a8a;display:block}
.dots{position:absolute;left:383px;width:675px;border-top:2px dotted var(--dots)}
.column{position:absolute;top:742px;width:315px;font-size:9.6px;line-height:12.6px}
.column p+p{margin-top:12.6px}
.column b{font-weight:400;color:var(--text-bright)}
.column a{color:var(--link)}
.copyright{position:absolute;left:383px;top:931px;font-size:9.6px;color:#8a8a8a}
</style>
</head>
<body>
<nav class="site-nav">
  <ul>
    <li class="is-active"><a href="#">Home</a></li>
    <li><a href="#">Design</a></li>
    <li><a href="#">Gallery</a></li>
    <li><a href="#">Quality</a></li>
    <li><a href="#">Contact Us</a></li>
    <li><a href="#">Links</a></li>
  </ul>
</nav>

<header class="brand">
  <span class="brand-mark"></span>
  <span class="brand-name">kitchen<br>atelier</span>
</header>

<div class="search">
  <span>Search here...</span>
  <span class="search-btn">
    <svg width="11" height="11" viewBox="0 0 11 11"><circle cx="4.5" cy="4.5" r="3.2" fill="none" stroke="#222" stroke-width="1.4"/><line x1="7" y1="7" x2="10" y2="10" stroke="#222" stroke-width="1.6"/></svg>
  </span>
</div>

<div class="glow-line" style="top:153px"></div>

<div class="thumb" style="top:175px;background:linear-gradient(100deg,#e1d6b8,#cbb48e 50%,#9c3e26 75%,#d8cfb4)" role="img" aria-label="Kitchen photo: stone arch and cherry cabinets"></div>
<div class="thumb" style="top:287px;background:linear-gradient(#bdbdbd,#8d8d8d 60%,#3a3a3a)" role="img" aria-label="Kitchen photo: modern white kitchen in black and white"></div>
<div class="thumb" style="top:399px;background:linear-gradient(#9a9a9a,#cfcfcf 60%,#5a5a5a)" role="img" aria-label="Kitchen photo: bright open kitchen in black and white"></div>
<div class="thumb" style="top:511px;background:linear-gradient(90deg,#2a2a2a,#6a6a6a 50%,#cfcfcf)" role="img" aria-label="Kitchen photo: dark cabinets and steel fridge in black and white"></div>

<div class="hero" role="img" aria-label="Slideshow photo: kitchen with stone arch, pendant lights and cherry wood island"></div>

<div class="glow-line" style="top:627px"></div>

<p class="social-label">Connect with us on:</p>
<a class="social" style="top:710px">+ FRIENDSPACE</a>
<a class="social" style="top:739px">+ CHIRPLINE</a>

<h1 class="content-title"><i></i>Designer Kitchens by Kitchen Atelier</h1>
<div class="dots" style="top:719px"></div>

<div class="column" style="left:383px">
  <p>Welcome to <b>Kitchen Atelier.</b> Westshire's exclusive kitchen manufacturer based in Harbourvale Marlow. If you are seeking the highest quality kitchen, yet at a price that is a little more affordable, Kitchen Atelier is the company you've been searching for.</p>
  <p><b>Kitchen Atelier</b> showroom is located less than 25 kilometers from Marlow CBD, so easy to get to with easy access from the Ridgeway Motorway.</p>
</div>
<div class="column" style="left:736px">
  <p>On this site, you can view some of our <b>designer kitchens</b>, read testimonials from our clients or just browse through our site to find out more. We hope you will find our site inspiring and put Kitchen Atelier at the top of your list of <b>kitchen showrooms</b> you simply must visit.</p>
  <p>Pop into our showroom. We can chat about your plans and ideas for your new kitchen and maybe we can give you a few ideas of our own. Or <a href="#">contact us</a> to arrange a no obligation consultation with one of our <b>kitchen designers</b> and if required we will bring the showroom to you.</p>
</div>

<div class="dots" style="top:916px"></div>
<p class="copyright">© 2010 Kitchen Atelier</p>
</body>
</html>
```